Property Management Company Business Cards

Need business cards for a property management company located in Michigan. We manage houses for clients all over the world. Young and modern company, looking for eye catching design. Please work with the attached logo.

Industry/Entity Type

Property Management

Requirements
Must have
• Need lines for address, telephone number, fax number, web site.

Also lines for name, and job title

```html
<!DOCTYPE html>
<html lang="en">
<head>
<meta charset="UTF-8">
<title>Lakeshore Crest Management – Business Cards</title>
<link rel="stylesheet" href="https://fonts.googleapis.com/css2?family=Source+Sans+3:wght@400;600;700&display=swap">
<style>
  :root {
    --backdrop: #e6e4e2;
    --card-white: #ffffff;
    --card-dark: #2f3235;
    --ink-dark: #2a2c2f;
    --accent-cyan: #3cc6ee;
    --rule-grey: #4a4d51;
    --text-light: #ffffff;
  }
  * { margin: 0; padding: 0; box-sizing: border-box; }
  html, body {
    width: 1200px;
    height: 1151px;
    overflow: hidden;
    background: var(--backdrop);
    font-family: "Source Sans 3", "Myriad Pro", Arial, sans-serif;
  }
  .canvas { position: relative; width: 1200px; height: 1151px; }

  .card {
    position: absolute;
    left: 220px;
    width: 760px;
    height: 434px;
    border-radius: 28px;
    overflow: hidden;
    box-shadow: 0 6px 18px rgba(0,0,0,0.18);
  }
  .card-front { top: 110px; background: var(--card-white); }
  .card-back  { top: 610px; background: var(--card-dark); }

  /* Front */
  .person {
    position: absolute;
    right: 62px;
    top: 118px;
    text-align: right;
    color: var(--accent-cyan);
  }
  .person-name { font-size: 31px; font-weight: 400; letter-spacing: 0.01em; }
  .person-title { font-size: 19px; font-weight: 400; margin-top: 2px; }

  .brand {
    position: absolute;
    left: 58px;
    top: 258px;
    display: flex;
    align-items: center;
    gap: 12px;
  }
  .brand-dot {
    width: 30px; height: 30px;
    border-radius: 50%;
    background: var(--accent-cyan);
    flex: none;
  }
  .brand-name {
    color: var(--ink-dark);
    font-weight: 700;
    line-height: 1;
  }
  .brand-name .line-main { display: block; font-size: 30px; letter-spacing: -0.01em; }
  .brand-name .line-sub { display: block; font-size: 13px; letter-spacing: 0.62em; margin-top: 4px; }

  .divider {
    position: absolute;
    left: 432px;
    top: 232px;
    width: 2px;
    height: 78px;
    background: var(--rule-grey);
  }

  .contact-icons {
    position: absolute;
    left: 454px;
    top: 236px;
    display: flex;
    flex-direction: column;
    gap: 10px;
  }
  .contact-icons svg { width: 16px; height: 16px; display: block; }

  .contact-lines {
    position: absolute;
    right: 62px;
    top: 252px;
    text-align: right;
    color: var(--ink-dark);
    font-size: 19px;
    line-height: 1.35;
  }

  /* Back */
  .back-brand {
    position: absolute;
    left: 0; right: 0;
    top: 150px;
    text-align: center;
    color: var(--text-light);
    font-weight: 700;
    line-height: 1;
  }
  .back-brand .line-main { display: block; font-size: 52px; letter-spacing: 0.005em; }
  .back-brand .line-sub { display: block; font-size: 21px; letter-spacing: 0.72em; margin-top: 8px; padding-left: 0.72em; }
  .back-web {
    position: absolute;
    left: 0; right: 0;
    top: 272px;
    text-align: center;
    color: var(--accent-cyan);
    font-size: 22px;
    letter-spacing: 0.12em;
  }
</style>
</head>
<body>
<main class="canvas">

  <section class="card card-front" aria-label="Business card front">
    <div class="person">
      <div class="person-name">YOUR NAME HERE</div>
      <div class="person-title">Job Title</div>
    </div>

    <div class="brand">
      <span class="brand-dot"></span>
      <span class="brand-name">
        <span class="line-main">LAKESHORE CREST</span>
        <span class="line-sub">MANAGEMENT</span>
      </span>
    </div>

    <div class="divider"></div>

    <div class="contact-icons" aria-hidden="true">
      <svg viewBox="0 0 16 16" class="icon-phone">
        <path d="M4 1.5 L6.5 4.5 L5 6.3 C5.8 8.2 7.8 10.2 9.7 11 L11.5 9.5 L14.5 12 L12.6 14.3 C7.5 13.6 2.4 8.5 1.7 3.4 Z" fill="var(--accent-cyan)"/>
      </svg>
      <svg viewBox="0 0 16 16" class="icon-fax">
        <rect x="4" y="1.5" width="8" height="5" fill="var(--accent-cyan)"/>
        <rect x="1.5" y="6" width="13" height="6" rx="1" fill="var(--accent-cyan)"/>
        <rect x="4" y="10" width="8" height="4.5" fill="var(--accent-cyan)" stroke="#fff" stroke-width="1"/>
      </svg>
      <svg viewBox="0 0 16 16" class="icon-mail">
        <rect x="1.5" y="3.5" width="13" height="9" fill="var(--accent-cyan)"/>
        <path d="M1.5 3.5 L8 9 L14.5 3.5" fill="none" stroke="#fff" stroke-width="1.2"/>
      </svg>
    </div>

    <div class="contact-lines">
      <div class="contact-phone">+0012 3456 7891</div>
      <div class="contact-fax">+0012 3456 7891</div>
      <div class="contact-address">YOUR ADRESS HERE</div>
    </div>
  </section>

  <section class="card card-back" aria-label="Business card back">
    <div class="back-brand">
      <span class="line-main">LAKESHORE CREST</span>
      <span class="line-sub">MANAGEMENT</span>
    </div>
    <div class="back-web">wwwwwww@wwwww.www.com</div>
  </section>

</main>
</body>
</html>
```